Meadowbrook Care Clinic needs a newspaper ad design

We need a newspaper ad for our Care Clinic. We provide primary medical care, medicated addiction therapy, psychiatric care, and psychotherapy in person and would really like to promote our teletherapy. So I have attached our company logo as well.

```html
<!DOCTYPE html>
<html lang="en">
<head>
<meta charset="utf-8">
<title>Meadowbrook Care Clinic – Family Medicine Practice Ad</title>
<link href="https://fonts.googleapis.com/css2?family=Montserrat:wght@400;600;700;800&display=swap" rel="stylesheet">
<style>
  :root {
    --canvas: #e7e7e7;
    --paper: #ffffff;
    --ink: #1a1a1a;
    --red: #f00f12;
    --blue: #0a14f0;
    --rule: #8a8a8a;
    --photo-warm: #d9b88e;
    --photo-light: #f3efe9;
  }
  * { box-sizing: border-box; margin: 0; padding: 0; }
  html, body { width: 800px; height: 1200px; overflow: hidden; }
  body {
    background: var(--canvas);
    font-family: "Montserrat", Arial, sans-serif;
    color: var(--ink);
    position: relative;
  }
  .ad {
    position: absolute;
    left: 30px; top: 339px;
    width: 740px; height: 522px;
    background: var(--paper);
    box-shadow: 0 6px 18px rgba(0,0,0,0.12);
    overflow: hidden;
  }
  .ad__photo {
    position: absolute;
    left: 300px; top: 0;
    width: 440px; height: 333px;
    background:
      linear-gradient(90deg, var(--paper) 0%, rgba(255,255,255,0) 28%),
      linear-gradient(100deg, var(--photo-light) 20%, #eadccb 55%, var(--photo-warm) 85%, #c49a6c 100%);
  }
  .brand {
    position: absolute; left: 42px; top: 42px;
    display: flex; align-items: center; gap: 8px;
  }
  .brand__mark { width: 14px; height: 14px; background: var(--red); }
  .brand__name { font-size: 17px; font-weight: 600; color: var(--ink); }
  .brand__tagline {
    position: absolute; left: 64px; top: 64px;
    font-size: 10.5px; color: #333;
  }
  .headline { position: absolute; left: 40px; top: 100px; }
  .headline__main {
    font-size: 56px; font-weight: 800; letter-spacing: -2px; line-height: 50px;
  }
  .headline__sub {
    font-size: 27px; font-weight: 800; color: var(--red);
    letter-spacing: -0.8px; line-height: 30px; margin-top: 4px;
  }
  .divider {
    position: absolute; left: 43px; top: 203px;
    width: 282px; height: 1px; background: var(--rule);
  }
  .divider::before {
    content: ""; position: absolute; left: 17px; top: -2px;
    width: 35px; height: 4px; border-radius: 2px; background: var(--red);
  }
  .intro {
    position: absolute; left: 43px; top: 216px; width: 290px;
    font-size: 10px; line-height: 13px; color: #333;
  }
  .services-tab {
    position: absolute; left: 0; top: 296px; width: 232px; height: 36px;
    background: var(--red);
    clip-path: polygon(0 0, 196px 0, 232px 100%, 0 100%);
    color: var(--paper); font-size: 18px; font-weight: 800;
    padding-left: 47px; line-height: 37px;
  }
  .services {
    position: absolute; left: 0; top: 336px; width: 740px; height: 100px;
    background: var(--blue);
    display: flex; padding: 20px 0 0 50px;
  }
  .services__col { list-style: none; }
  .services__col:nth-child(1) { width: 270px; }
  .services__col:nth-child(2) { width: 205px; }
  .services__item {
    display: flex; align-items: center; gap: 8px;
    color: var(--paper); font-size: 11px; font-weight: 700;
    height: 17px;
  }
  .services__item svg { width: 10px; height: 10px; flex: none; }
  .contact { position: absolute; left: 48px; top: 446px; width: 280px; }
  .contact__call { display: flex; align-items: baseline; gap: 6px; white-space: nowrap; }
  .contact__label { color: var(--red); font-size: 14px; font-weight: 700; }
  .contact__phone { font-size: 21px; font-weight: 800; }
  .contact__web { display: flex; align-items: center; gap: 12px; margin-top: 4px; white-space: nowrap; }
  .contact__web svg { width: 18px; height: 18px; flex: none; }
  .contact__url { font-size: 15px; font-weight: 600; letter-spacing: 0.3px; }
  .separator {
    position: absolute; left: 340px; top: 452px; width: 3px; height: 46px;
    background: radial-gradient(circle, var(--ink) 1.3px, transparent 1.6px) 0 0 / 3px 8px repeat-y;
  }
  .hours { position: absolute; left: 367px; top: 452px; font-size: 10.5px; font-weight: 700; line-height: 14px; }
  .hours__crisis { color: var(--red); }
  .hours__days { margin-top: 5px; }
  .hours__days span { color: var(--red); }
</style>
</head>
<body>
  <article class="ad">
    <div class="ad__photo" role="img" aria-label="Photo of a senior doctor with a headset speaking during a video call at a laptop in a bright office"></div>

    <div class="brand">
      <span class="brand__mark"></span>
      <span class="brand__name">Meadowbrook Care Clinic</span>
    </div>
    <p class="brand__tagline">Dedicated to Hope, Healing &amp; Recovery</p>

    <h1 class="headline">
      <div class="headline__main">FAMILY</div>
      <div class="headline__sub">MEDICINE PRACTICE</div>
    </h1>
    <div class="divider"></div>

    <p class="intro">Meadowbrook Care Clinic is a family focused medical and mental health care practice. Specializing in the care of your family, including children, adolescents, adults, and seniors!</p>

    <div class="services-tab">OUR SERVICES</div>

    <section class="services">
      <ul class="services__col">
        <li class="services__item"><svg viewBox="0 0 10 10"><circle cx="5" cy="5" r="5" fill="#fff"/><path d="M2.7 5.2 4.3 6.7 7.3 3.5" stroke="#0a14f0" stroke-width="1.4" fill="none"/></svg>Behavioral Health – Individual Therapy</li>
        <li class="services__item"><svg viewBox="0 0 10 10"><circle cx="5" cy="5" r="5" fill="#fff"/><path d="M2.7 5.2 4.3 6.7 7.3 3.5" stroke="#0a14f0" stroke-width="1.4" fill="none"/></svg>Elder Care</li>
        <li class="services__item"><svg viewBox="0 0 10 10"><circle cx="5" cy="5" r="5" fill="#fff"/><path d="M2.7 5.2 4.3 6.7 7.3 3.5" stroke="#0a14f0" stroke-width="1.4" fill="none"/></svg>Grief Therapy</li>
        <li class="services__item"><svg viewBox="0 0 10 10"><circle cx="5" cy="5" r="5" fill="#fff"/><path d="M2.7 5.2 4.3 6.7 7.3 3.5" stroke="#0a14f0" stroke-width="1.4" fill="none"/></svg>Marital Counseling</li>
      </ul>
      <ul class="services__col">
        <li class="services__item"><svg viewBox="0 0 10 10"><circle cx="5" cy="5" r="5" fill="#fff"/><path d="M2.7 5.2 4.3 6.7 7.3 3.5" stroke="#0a14f0" stroke-width="1.4" fill="none"/></svg>Psychological Evaluations</li>
        <li class="services__item"><svg viewBox="0 0 10 10"><circle cx="5" cy="5" r="5" fill="#fff"/><path d="M2.7 5.2 4.3 6.7 7.3 3.5" stroke="#0a14f0" stroke-width="1.4" fill="none"/></svg>School Issues</li>
        <li class="services__item"><svg viewBox="0 0 10 10"><circle cx="5" cy="5" r="5" fill="#fff"/><path d="M2.7 5.2 4.3 6.7 7.3 3.5" stroke="#0a14f0" stroke-width="1.4" fill="none"/></svg>Trauma Therapy</li>
        <li class="services__item"><svg viewBox="0 0 10 10"><circle cx="5" cy="5" r="5" fill="#fff"/><path d="M2.7 5.2 4.3 6.7 7.3 3.5" stroke="#0a14f0" stroke-width="1.4" fill="none"/></svg>Crisis Therapy</li>
      </ul>
      <ul class="services__col">
        <li class="services__item"><svg viewBox="0 0 10 10"><circle cx="5" cy="5" r="5" fill="#fff"/><path d="M2.7 5.2 4.3 6.7 7.3 3.5" stroke="#0a14f0" stroke-width="1.4" fill="none"/></svg>Diabetes Care</li>
        <li class="services__item"><svg viewBox="0 0 10 10"><circle cx="5" cy="5" r="5" fill="#fff"/><path d="M2.7 5.2 4.3 6.7 7.3 3.5" stroke="#0a14f0" stroke-width="1.4" fill="none"/></svg>Asthma Treatment</li>
        <li class="services__item"><svg viewBox="0 0 10 10"><circle cx="5" cy="5" r="5" fill="#fff"/><path d="M2.7 5.2 4.3 6.7 7.3 3.5" stroke="#0a14f0" stroke-width="1.4" fill="none"/></svg>Chronic Health Conditions</li>
        <li class="services__item"><svg viewBox="0 0 10 10"><circle cx="5" cy="5" r="5" fill="#fff"/><path d="M2.7 5.2 4.3 6.7 7.3 3.5" stroke="#0a14f0" stroke-width="1.4" fill="none"/></svg>Colds, Flu, and Allergies</li>
      </ul>
    </section>

    <div class="contact">
      <div class="contact__call">
        <span class="contact__label">CALL US NOW:</span>
        <span class="contact__phone">555.014.2876</span>
      </div>
      <div class="contact__web">
        <svg viewBox="0 0 20 20"><circle cx="10" cy="10" r="9" fill="none" stroke="#f00f12" stroke-width="1.6"/><ellipse cx="10" cy="10" rx="4" ry="9" fill="none" stroke="#f00f12" stroke-width="1.4"/><path d="M1 10h18M3 5.5h14M3 14.5h14" stroke="#f00f12" stroke-width="1.3"/></svg>
        <span class="contact__url">www.meadowbrookcare.com</span>
      </div>
    </div>

    <div class="separator"></div>

    <div class="hours">
      <p>After hours and weekends available by appointment.</p>
      <p class="hours__crisis">Crisis services available 24/7.</p>
      <p class="hours__days"><span>Monday – Friday:</span> 8:30 AM – 5 PM</p>
    </div>
  </article>
</body>
</html>
```